LOMEX - Webdesign für eine Poolreinigungsfirma
A designer more than perfect. Impressive design, much more than we could ever have imagined. Very professional and quick work. One of the biggest talents of this page !
Zielgruppe
Wir sind LOMEX, eine junge Poolreinigungsfirma die gerade erst in den Startlöchern sitzt. Wir befinden uns auf der französischen Insel LA RÉUNION und richten uns an Personen jeglichen Alters, die einen Pool besitzen.
Aufgabenstellung
Wir wünschen uns ein in erster Linie LUXURIÖSES, schickes und sehr ansprechendes Webdesign, dass - unbedingt - die Verbindung zur Natur zeigt (Tropen, Beispielfotos im Anhang). Natur + Wasser / Pool.
BITTE KEINE TYPISCHE POOLWEBSITE, da wir u.a. auch bald in den Verkauf luxuriöser Accessoires gehen möchten. Wir möchten uns von der Konkurrenz stark und deutlich abheben.
Wir wünschen uns einen DUNKLEN MOOD (gerne auch schwarz auf weißem Hintergrund o.ä. ?).
Wir sind von AI-Bildern sehr angetan, da sie Träume erwecken und in der Tiefe ansprechen können. Nutzen Sie diese gerne, bieten Sie uns Vorschläge. Bitte passend zu den Tropen.
Wir überlassen Ihnen vertrauensvoll die Erstellung des Designs der Website (Aufbau, etc), wir möchten uns überraschen lassen.
Unser Logo, ein Briefing für drei gewünschte Seiten und Beispielbilder, die sehr gerne genutzt werden können (oder in Anlehnung an diese, gleicher Stil) sind im Anhang zu finden.
Die Seite sollte unbedingt - auch - die Nutzung mit Mobiltelefonen ermöglichen und keine Verzögerungen beim Aufrufen / Laden der Website aufzeigen.

```html
<!DOCTYPE html>
<html lang="fr">
<head>
<meta charset="utf-8">
<title>LOMEX – Entretien de piscine</title>
<link rel="stylesheet" href="https://fonts.googleapis.com/css2?family=Raleway:wght@300;400;500;600;700&family=Playfair+Display:wght@600;700&display=swap">
<style>
:root{
  --ink:#0c1011;
  --white:#ffffff;
  --text:#4a4f50;
  --teal:#3a9fa8;
  --teal-dark:#227f86;
  --icon:#2f9a8c;
  --leaf:#2d4a1f;
  --leaf-dark:#18300f;
}
*{margin:0;padding:0;box-sizing:border-box}
html,body{width:1200px;height:4541px;overflow:hidden;background:var(--white)}
body{position:relative;font-family:"Raleway",sans-serif;color:var(--text)}
.abs{position:absolute}
.serif{font-family:"Playfair Display",serif;font-weight:700;color:var(--ink);letter-spacing:-0.5px;text-transform:uppercase;line-height:1.05}

/* header */
.site-header{left:0;top:0;width:1200px;height:93px;background:var(--ink)}
.brand{left:106px;top:22px;width:84px;text-align:center;color:var(--white);font-weight:500;letter-spacing:3px;font-size:17px}
.brand .dot{display:block;width:26px;height:26px;border:2px solid var(--white);border-radius:50%;margin:0 auto 6px}
.main-nav{right:100px;top:0;height:93px;display:flex}
.main-nav a{color:var(--white);text-decoration:none;font-size:15px;letter-spacing:.3px;padding:38px 18px 0;height:93px;position:relative}
.main-nav a.active::after{content:"";position:absolute;left:0;right:0;bottom:0;height:4px;background:var(--teal)}

/* hero */
.hero{left:0;top:93px;width:1200px;height:473px;background:linear-gradient(180deg,#6f7a5a 0%,#a69c78 35%,#5e6a52 60%,#26302a 100%)}
.hero-title{left:0;top:232px;width:1200px;text-align:center;color:var(--white);font-family:"Raleway",sans-serif;font-weight:400;font-size:180px;letter-spacing:30px;line-height:180px;height:180px;margin-top:-30px}
.hero-sweep{left:0;top:520px;width:1200px;height:140px}

/* about */
.about-title{left:0;top:644px;width:1200px;text-align:center;font-size:44px}
.about-kicker{left:0;top:760px;width:1200px;text-align:center;font-size:19px;color:#3a3f40}
.about-copy{left:180px;top:810px;width:840px;text-align:center;font-size:14.5px;line-height:24px}
.about-copy p+p{margin-top:24px}
.about-copy b{font-weight:700;color:var(--ink)}

/* quote */
.quote-band{left:0;top:1065px;width:1200px;height:330px;background:var(--ink)}
.quote-text{left:120px;top:1130px;width:960px;text-align:center;color:var(--white);font-size:35px;line-height:44px;font-weight:400}
.quote-text strong{font-weight:600}
.quote-by{left:0;top:1290px;width:1200px;text-align:center;color:var(--white);font-size:19px}
.quote-mark{left:860px;top:1170px;font-family:"Playfair Display",serif;font-size:200px;color:#1d2324;line-height:1}

/* values */
.value{top:1472px;width:290px;text-align:center}
.value svg{display:block;margin:0 auto 6px}
.value h3{font-size:20px;font-weight:600;color:var(--teal-dark);line-height:24px;margin:0 auto 10px;width:230px}
.value p{font-size:14.5px;line-height:24px;padding:0 6px}
.value b{font-weight:700;color:var(--ink)}

/* respect */
.leaf{left:0;top:1985px;width:726px;height:680px;background:linear-gradient(135deg,#3d5e2a 0%,var(--leaf) 55%,var(--leaf-dark) 100%)}
.respect-photo{left:726px;top:2080px;width:474px;height:554px;background:linear-gradient(180deg,#2d3a2a 0%,#3f5a46 40%,#4f8a95 65%,#2f6b74 100%)}
.respect-photo .brand{left:38px;top:30px}
.respect-title{left:106px;top:2170px;width:520px;color:var(--white);font-size:46px}
.respect-copy{left:106px;top:2340px;width:520px;color:var(--white);font-size:14.5px;line-height:24px}
.respect-copy p+p{margin-top:24px}

/* partners */
.palm-left{left:0;top:2916px;width:238px;height:430px;background:linear-gradient(90deg,rgba(76,120,36,.55) 0%,rgba(76,120,36,0) 100%)}
.palm-right{left:1020px;top:3198px;width:180px;height:396px;background:linear-gradient(270deg,rgba(76,120,36,.55) 0%,rgba(76,120,36,0) 100%)}
.partners-title{left:0;top:2848px;width:1200px;text-align:center;font-size:46px}
.partners-copy{left:200px;top:2970px;width:800px;text-align:center;font-size:14.5px;line-height:24px}
.services-title{left:0;top:3100px;width:1200px;text-align:center;font-size:46px}
.services-sub{left:0;top:3172px;width:1200px;text-align:center;font-size:15px}

.card{display:flex;flex-direction:column;align-items:center;justify-content:center;text-align:center;color:var(--white);padding:0 10px}
.card h4{font-family:"Playfair Display",serif;font-weight:700;text-transform:uppercase;font-size:19px;line-height:24px}
.card p{font-size:14.5px;line-height:22px;margin-top:2px}
.card-weekly{left:109px;top:3267px;width:353px;height:462px;background:linear-gradient(160deg,#3a3a36 0%,#23231f 55%,#151513 100%)}
.card-weekly h4{font-size:31px;line-height:38px}
.card-weekly p{font-size:19px;line-height:28px;margin-top:14px}
.card-green{left:499px;top:3267px;width:282px;height:210px;background:linear-gradient(180deg,#1b2420,#101613)}
.card-absence{left:813px;top:3267px;width:282px;height:210px;background:linear-gradient(180deg,#1f3d27,#10251a)}
.card-cell{left:499px;top:3521px;width:282px;height:208px;background:linear-gradient(160deg,#1d7a55,#0d4f3a)}
.card-diag{left:813px;top:3521px;width:282px;height:208px;background:linear-gradient(160deg,#4ea9ae,#2e8c94)}
.card-diag h4{font-size:18px;white-space:nowrap}
.cta{left:479px;top:3787px;width:242px;height:65px;background:var(--teal);color:var(--white);font-size:15px;display:flex;align-items:center;justify-content:center;text-decoration:none;letter-spacing:.3px}

/* footer */
.site-footer{left:0;top:3923px;width:1200px;height:618px;background:linear-gradient(120deg,#0b1210 0%,#15241b 40%,#2d4a28 60%,#173a36 85%,#0d2326 100%)}
.footer-brand{left:160px;top:4040px;width:156px;text-align:center;color:var(--white);font-size:30px;letter-spacing:5px;font-weight:500}
.footer-brand .dot{display:block;width:44px;height:44px;border:3px solid var(--white);border-radius:50%;margin:0 auto 10px}
.social{top:4188px;width:28px;height:28px;border-radius:50%;background:var(--white)}
.contact-card{left:106px;top:4240px;width:301px;height:301px;background:var(--white);padding:30px 20px 0}
.contact-card h5{font-family:"Playfair Display",serif;font-weight:700;font-size:23px;color:var(--ink);text-transform:uppercase;margin-bottom:10px}
.contact-card p{font-size:14px;line-height:24px}
.contact-rows{margin-top:28px}
.contact-row{display:flex;font-size:13.5px;line-height:22px}
.contact-row span:first-child{width:128px;font-weight:700;color:var(--ink)}
</style>
</head>
<body>

<header class="abs site-header">
  <div class="abs brand"><span class="dot"></span>LOMEX</div>
  <nav class="abs main-nav">
    <a href="#" class="active">PAGE D'ACCUEIL</a>
    <a href="#">NOS PRESTATIONS</a>
    <a href="#">CARRIÈRES</a>
    <a href="#">CONTACT</a>
  </nav>
</header>

<section class="abs hero" role="img" aria-label="Piscine à débordement au cœur d'une forêt tropicale au lever du soleil"></section>
<div class="abs hero-title">LOMEX</div>
<svg class="abs hero-sweep" viewBox="0 0 1200 140" preserveAspectRatio="none" aria-hidden="true">
  <defs><linearGradient id="sweep" x1="0" x2="1"><stop offset="0" stop-color="#fff" stop-opacity="0"/><stop offset="1" stop-color="#000" stop-opacity=".12"/></linearGradient></defs>
  <path d="M700 46 L1200 46 L1200 120 Z" fill="url(#sweep)"/>
</svg>

<h1 class="abs serif about-title">L'entretien de<br>votre piscine</h1>
<div class="abs about-kicker">À PROPOS DE NOUS</div>
<div class="abs about-copy">
  <p><b>LOMEX</b>, un mot simple qui réunit „Lotus &amp; Mer", symbole du respect de la nature et de l'environnement. Mettant en avant le luxe et la qualité <b>LOMEX</b> propose la création d'un espace d'eau reposant pour pouvoir se recentrer sur soi-même et les essentiels de la vie.</p>
  <p>Parce que l'entretien et le nettoyage d'une piscine nécessitent de réelles connaissances, choisir <b>LOMEX</b> c'est la certitude d'un service impeccable et de haut de gamme. Profitez des prestations uniques en exclusivité, savourez votre eau claire et limpide pour une expérience innovante exceptionnelle.</p>
</div>

<section class="abs quote-band"></section>
<div class="abs quote-mark" aria-hidden="true">"</div>
<blockquote class="abs quote-text">C'est un profond plaisir de rendre <strong>le meilleur service</strong> possible pour contribuer à des moments inoubliables autour de la piscine.</blockquote>
<div class="abs quote-by">Dirigeant, <strong>LOMEX</strong></div>

<article class="abs value" style="left:102px">
  <svg width="70" height="66" viewBox="0 0 70 66" fill="none" stroke="var(--icon)" stroke-width="2.2"><circle cx="26" cy="24" r="8"/><path d="M12 62 V46 q0-8 14-8 q14 0 14 8 V62"/><circle cx="50" cy="16" r="11"/><path d="M43 26 L36 40"/></svg>
  <h3>NOUS SERVONS NOS CLIENTS</h3>
  <p>Nous nous adressons aux particuliers, professionnels, locations saisonnières et bien plus. Avec passion et soin nous proposons toujours le meilleur service adapté à vos besoins personnels car votre satisfaction est notre priorité. <b>LOMEX</b> sert ses clients avec professionnalisme, qualité et honnêteté.</p>
</article>
<article class="abs value" style="left:463px">
  <svg width="70" height="66" viewBox="0 0 70 66" fill="none" stroke="var(--icon)" stroke-width="2.2"><path d="M35 10 L42 26 L59 27 L46 38 L50 55 L35 46 L20 55 L24 38 L11 27 L28 26 Z"/><path d="M35 2 v4 M8 14 l4 3 M62 14 l-4 3"/></svg>
  <h3>CONFIANCE</h3>
  <p>Les craintes et contraintes liées à la possession de votre piscine prennent fin avec la décision de plonger dans le monde exclusif de <b>LOMEX</b>. Notre professionnalisme vous accompagnera tout au long de votre contrat d'entretien piscine.</p>
</article>
<article class="abs value" style="left:825px">
  <svg width="70" height="66" viewBox="0 0 70 66" fill="none" stroke="var(--icon)" stroke-width="2.2"><path d="M26 6 C18 18 12 26 12 34 a14 14 0 0 0 28 0 C40 26 34 18 26 6Z"/><circle cx="42" cy="40" r="12"/><path d="M36 40 l4 4 l8 -8 M51 49 l10 10"/></svg>
  <h3>VOTRE PISCINE</h3>
  <p><b>LOMEX</b> garantie une eau claire et limpide. Les passages réguliers permettent une analyse de la qualité de l'eau ainsi qu'un contrôle de vos installations afin de prévenir un dysfonctionnement et prolonger la durée de vie du matériel et de ses revêtements. Profitez de votre piscine en toute tranquillité.</p>
</article>

<div class="abs leaf" role="img" aria-label="Grande feuille tropicale verte en fond"></div>
<h2 class="abs serif respect-title">Respect de votre santé et de l'environnement</h2>
<div class="abs respect-copy">
  <p><strong>LOMEX</strong>, symbole du respect de la nature, met toujours en avant le respect total de la santé des baigneurs, leurs bien-être et celle de l'environnement. Ayant conscience des nombreux dangers de l'utilisation des produits chimiques, nous vous accompagnerons avec la plus grande exigence. Pour ne pas oublier et perdre les bienfaits de votre piscine, nous adaptons minutieusement le bon dosage des produits chimiques.</p>
  <p>En les maîtrisant, nous ne respectons pas juste le corps humain, mais également la totalité de votre environnement. <strong>LOMEX</strong> s'engage pour un monde meilleur, responsable et écologique.</p>
</div>
<div class="abs respect-photo" role="img" aria-label="Bouée orange flottant sur une piscine entourée de végétation tropicale">
  <div class="abs brand"><span class="dot"></span>LOMEX</div>
</div>

<div class="abs palm-left" role="img" aria-label="Feuilles de palmier en bordure gauche"></div>
<div class="abs palm-right" role="img" aria-label="Feuilles de palmier en bordure droite"></div>

<h2 class="abs serif partners-title">Collaborations avec nos<br>partenaires</h2>
<p class="abs partners-copy">En cas de détection d'un dysfonctionnement par notre équipe, nous vous proposons une intervention par nos partenaires certifiés et professionnels. Pour que vous retrouvez rapidement votre piscine en état de plein fonctionnement.</p>
<h2 class="abs serif services-title">Nos prestations</h2>
<p class="abs services-sub">Nos prestations sont adaptées à vos besoins individuels.</p>

<div class="abs card card-weekly" role="img" aria-label="Escalier de piscine sous les ombres de palmes"><h4>Intervention<br>hebdomadaire</h4><p>4 passages par mois, produits<br>d'entretien inclus</p></div>
<div class="abs card card-green" role="img" aria-label="Piscine dans un jardin sombre"><h4>Rattrapage eau verte</h4></div>
<div class="abs card card-absence" role="img" aria-label="Piscine entourée de plantes tropicales"><h4>Passage ponctuel<br>pendant<br>votre absence</h4></div>
<div class="abs card card-cell" role="img" aria-label="Bulles d'eau vertes"><h4>Détartrage de la<br>cellule<br>d'électrolyseur</h4></div>
<div class="abs card card-diag" role="img" aria-label="Villa moderne avec piscine turquoise"><h4>Diagnostique, conseils,</h4><p>analyse, rééquilibrage des<br>paramètres<br>de l'eau à votre domicile</p></div>

<a class="abs cta" href="#">CONTACTEZ-NOUS</a>

<footer class="abs site-footer" role="img" aria-label="Plantes tropicales se reflétant dans l'eau d'une piscine de nuit"></footer>
<div class="abs footer-brand"><span class="dot"></span>LOMEX</div>
<span class="abs social" style="left:202px"></span>
<span class="abs social" style="left:244px"></span>
<div class="abs contact-card">
  <h5>Contact LOMEX</h5>
  <p>Vous offrir une prestation de qualité c'est notre priorité afin de maintenir l'esthétisme de votre piscine et vous procurer entière satisfaction.</p>
  <div class="contact-rows">
    <div class="contact-row"><span>MAIL</span><span>contact@lomex.re</span></div>
    <div class="contact-row"><span>TÉLÉPHONE</span><span>0692 41 28 15</span></div>
  </div>
</div>

</body>
</html>
```